KT-Systems advertising flag and billboard design

I need a design for advertising flag and a design for billboard.
Information can be obtained from https://kt-sytronik.de.
Updates
Target Market(s)
IT service for companies
Requirements
Must have
- Logo, contact information and services

```html
<!DOCTYPE html>
<html lang="de">
<head>
<meta charset="utf-8">
<title>KT-Systems – Billboard</title>
<link rel="stylesheet" href="https://fonts.googleapis.com/css2?family=Open+Sans:wght@400;600;800&display=swap">
<style>
  :root {
    --page-bg: #f2f2f4;
    --board-light: #eef0f6;
    --board-mid: #9aa6d6;
    --board-deep: #5a5aa8;
    --purple: #8754dc;
    --lavender: #dcc6fb;
    --brand-blue: #0a0ac8;
    --ink: #111118;
    --white: #ffffff;
  }
  * { margin: 0; padding: 0; box-sizing: border-box; }
  html, body {
    width: 1200px; height: 846px; overflow: hidden;
    background: var(--page-bg);
    font-family: "Open Sans", sans-serif;
  }
  .billboard {
    position: absolute; left: 20px; top: 213px;
    width: 1160px; height: 420px; overflow: hidden;
    background: linear-gradient(100deg, var(--board-light) 0%, #d6dcee 25%, var(--board-mid) 50%, var(--board-deep) 75%, #3a3a86 100%);
    box-shadow: 0 10px 30px rgba(0,0,0,.18);
  }
  .billboard__art { position: absolute; inset: 0; width: 100%; height: 100%; }
  .brand {
    position: absolute; left: 56px; top: 22px;
    font-weight: 800; font-size: 66px; letter-spacing: 2px;
    color: var(--brand-blue); text-transform: uppercase;
  }
  .services {
    position: absolute; left: 60px; top: 122px;
    list-style: none; font-size: 17px; font-weight: 600; color: var(--ink);
    line-height: 24px;
  }
  .services li::before { content: "• "; }
  .contact-email {
    position: absolute; left: 300px; top: 292px;
    display: flex; align-items: center; gap: 8px;
    font-size: 20px; font-weight: 800; color: var(--ink);
  }
  .contact-phone {
    position: absolute; left: 56px; top: 318px;
    font-size: 56px; font-weight: 800; letter-spacing: 5px;
    color: var(--brand-blue);
  }
</style>
</head>
<body>
<section class="billboard">
  <svg class="billboard__art" viewBox="0 0 1160 420" aria-hidden="false">
    <defs>
      <linearGradient id="photoTone" x1="0" y1="0" x2="1" y2="1">
        <stop offset="0" stop-color="#e6e9ef"/>
        <stop offset=".55" stop-color="#f4f1ee"/>
        <stop offset="1" stop-color="#c99a7c"/>
      </linearGradient>
    </defs>
    <polygon class="panel-purple" points="800,0 1160,0 1160,420 770,420 830,350 770,170" fill="var(--purple)"/>
    <polygon class="panel-lavender" points="700,160 800,110 850,160 760,250" fill="var(--lavender)"/>
    <polygon class="panel-lavender" points="1080,200 1160,140 1160,330 1120,300" fill="var(--lavender)"/>
    <polygon class="photo-frame" points="760,215 850,88 1060,88 1125,225 1050,385 850,385" fill="var(--white)"/>
    <polygon class="photo" role="img" aria-label="Foto: zwei lachende Kollegen arbeiten gemeinsam am Laptop" points="775,215 858,100 1052,100 1110,225 1042,372 858,372" fill="url(#photoTone)"/>
  </svg>

  <div class="brand">KT-Systems</div>

  <ul class="services">
    <li>Firewall-Lösungen</li>
    <li>Antivierensysteme</li>
    <li>Software Lösungen</li>
    <li>IT-Infrastruktur Modernisierung</li>
    <li>E-mail-Sicherhelt</li>
    <li>Cloud-Lösungen</li>
    <li>Hardware Lösungen</li>
  </ul>

  <div class="contact-email">
    <svg width="26" height="18" viewBox="0 0 26 18" aria-hidden="true">
      <rect x="1" y="1" width="24" height="16" fill="none" stroke="var(--ink)" stroke-width="1.6"/>
      <polyline points="1,1 13,10 25,1" fill="none" stroke="var(--ink)" stroke-width="1.6"/>
    </svg>
    <span>info@kt-s.de</span>
  </div>

  <div class="contact-phone">01234-5678901</div>
</section>
</body>
</html>
```